Business Card Design

We need a business card designed for our new company. Prefer a black card with white logo & writing.

Contact Information for Business Card

Dov Telling, address: 3-4817 Fernwick Avenue, Abbotsford, BC, V8K 2P9, Office Phone: 604-913-2760, Cell: 604-271-4053, Email: dov@qlresinhaus.ca

Colors

Designer to choose only greyscale colors for use in the design.

```html
<!DOCTYPE html>
<html lang="en">
<head>
<meta charset="utf-8">
<title>QL Resin Haus — Business Card</title>
<link href="https://fonts.googleapis.com/css2?family=Montserrat:wght@400;500;700&display=swap" rel="stylesheet">
<style>
  :root {
    --backdrop: #1f1f1f;
    --card: #000000;
    --ink: #ffffff;
    --ink-soft: #e6e6e6;
  }
  * { margin: 0; padding: 0; box-sizing: border-box; }
  html, body {
    width: 1200px;
    height: 900px;
    overflow: hidden;
    background: var(--backdrop);
    font-family: "Montserrat", Arial, sans-serif;
    color: var(--ink);
  }
  .card {
    position: absolute;
    left: 341px;
    width: 518px;
    height: 296px;
    background: var(--card);
  }
  .card--front { top: 141px; }
  .card--back { top: 463px; }

  .brand {
    position: absolute;
    display: flex;
    align-items: center;
    transform: translate(-50%, -50%);
    white-space: nowrap;
    font-weight: 700;
    color: var(--ink);
  }
  .brand__dot {
    border-radius: 50%;
    background: var(--ink);
    flex: none;
  }
  .card--front .brand { left: 150px; top: 148px; font-size: 19px; letter-spacing: 0.5px; gap: 7px; }
  .card--front .brand__dot { width: 9px; height: 9px; }
  .card--back .brand { left: 259px; top: 148px; font-size: 30px; letter-spacing: 0.8px; gap: 11px; }
  .card--back .brand__dot { width: 14px; height: 14px; }

  .divider {
    position: absolute;
    left: 260px;
    top: 83px;
    width: 1.5px;
    height: 130px;
    background: var(--ink);
  }
  .contact {
    position: absolute;
    left: 285px;
    top: 79px;
  }
  .contact__name {
    font-size: 18px;
    font-weight: 700;
    letter-spacing: 0.3px;
    line-height: 22px;
    text-transform: uppercase;
  }
  .contact__address {
    margin-top: 12px;
    font-size: 13.5px;
    font-weight: 400;
    line-height: 18px;
    color: var(--ink-soft);
  }
  .contact__lines {
    margin-top: 12px;
    list-style: none;
    font-size: 13.5px;
    line-height: 18px;
    color: var(--ink-soft);
  }
  .contact__lines li { display: flex; align-items: center; gap: 6px; }
  .contact__icon { width: 12px; height: 12px; fill: var(--ink); flex: none; }

  .website {
    position: absolute;
    left: 0;
    right: 0;
    top: 256px;
    text-align: center;
    font-size: 12.5px;
    letter-spacing: 1.2px;
    font-weight: 400;
  }
  .website strong { font-weight: 700; }
</style>
</head>
<body>
  <section class="card card--front">
    <div class="brand"><span class="brand__dot"></span>QL RESIN HAUS</div>
    <div class="divider"></div>
    <div class="contact">
      <p class="contact__name">Dov Telling</p>
      <p class="contact__address">3-4817 Fernwick Avenue<br>Abbotsford, BC, V8K 2P9</p>
      <ul class="contact__lines">
        <li>
          <svg class="contact__icon" viewBox="0 0 24 24" aria-hidden="true"><path d="M6.6 10.8a15.1 15.1 0 0 0 6.6 6.6l2.2-2.2a1 1 0 0 1 1-.25 11.4 11.4 0 0 0 3.6.57 1 1 0 0 1 1 1V20a1 1 0 0 1-1 1A17 17 0 0 1 3 4a1 1 0 0 1 1-1h3.5a1 1 0 0 1 1 1c0 1.25.2 2.45.57 3.57a1 1 0 0 1-.25 1z"/></svg>
          604-913-2760
        </li>
        <li>
          <svg class="contact__icon" viewBox="0 0 24 24" aria-hidden="true"><path d="M8 1h8a2 2 0 0 1 2 2v18a2 2 0 0 1-2 2H8a2 2 0 0 1-2-2V3a2 2 0 0 1 2-2zm0 3v15h8V4zm4 16.2a.9.9 0 1 0 0 1.8.9.9 0 0 0 0-1.8z"/></svg>
          604-271-4053
        </li>
        <li>
          <svg class="contact__icon" viewBox="0 0 24 24" aria-hidden="true"><path d="M2 5h20v2.2l-10 6.3L2 7.2zm0 4.6 10 6.3 10-6.3V19H2z"/></svg>
          dov@qlresinhaus.ca
        </li>
      </ul>
    </div>
    <p class="website">www.<strong>qlresinhaus</strong>.ca</p>
  </section>

  <section class="card card--back">
    <div class="brand"><span class="brand__dot"></span>QL RESIN HAUS</div>
  </section>
</body>
</html>
```